Mathis Verbeke - Magician and Mentalist

I am a professional magician - mentalist based in Belgium. My stage name is Mathis Verbeke. I need a flyer (that I could use electronically or in print) to promote my activity. The flyer should represent myself "hand drawn" together with some classical attributes of a magician / mentalist : playing cards, billets, a crystal ball, some items related to mystery and conjuring... My logo has already been designed and I attach it enclosed. I also enclose a few pictures of me and a previous drawing that was made by a friend, but I am not satisfied with. As an example of what I like, I very much like the graphics of the poster of "Hollow Signals" (also enclosed). But it can be something totally different. See also my website for some graphic "feeling" : www.mathisverbeke.be

Target Market(s)

General public

Industry/Entity Type

Magician

Font styles to use
Other font styles liked:
• Old Newspaper Types (font enclosed in the uploaded files)

Colors

Designer to choose colors to be used in the design.

Requirements
Must have
• The project should reflect mystery/conjuring, and some items related to it (mainly playing cards but other elements may be inserted : a dice, ESP symbols, a "?" sign. Please see the enclosed files also.
Should not have
• I am not a "traditional" magician, so classic magic-related items like a hat, or a rabbit, or silks... should not appear in the design please.

```html
<!DOCTYPE html>
<html lang="en">
<head>
<meta charset="utf-8">
<title>Mathis Verbeke – Magician &amp; Mentalist</title>
<link href="https://fonts.googleapis.com/css2?family=Rye&family=Graduate&family=PT+Sans:wght@400;700&display=swap" rel="stylesheet">
<style>
  :root {
    --night-deep: #07090c;
    --night-teal: #1b3038;
    --night-mid: #102027;
    --horizon-glow: #2f6a86;
    --ribbon-red: #e2392f;
    --ribbon-shade: #b02a22;
    --paper-white: #ffffff;
    --moon-light: #eef2f6;
    --moon-shadow: #9fb0c2;
    --logo-grey: #4a4a4a;
    --symbol-grey: #8b8b8b;
    --link-red: #e0392c;
    --card-cream: #e9e1c8;
    --card-white: #f4f2ee;
    --portrait-light: #8a7d73;
    --portrait-dark: #2a2826;
  }
  * { margin: 0; padding: 0; box-sizing: border-box; }
  html, body { width: 873px; height: 1200px; overflow: hidden; background: var(--night-deep); }

  .poster {
    position: relative;
    width: 873px;
    height: 1200px;
    overflow: hidden;
    background: linear-gradient(180deg, var(--night-teal) 0%, var(--night-mid) 40%, #0c171c 62%, var(--night-deep) 100%);
  }

  .scene-backdrop {
    position: absolute; inset: 0;
    background:
      radial-gradient(ellipse 60% 8% at 50% 67%, rgba(47,106,134,0.55), transparent 70%),
      radial-gradient(ellipse 80% 40% at 50% 15%, rgba(60,90,100,0.35), transparent 70%);
  }

  .portrait {
    position: absolute;
    left: 150px; top: 170px;
    width: 574px; height: 610px;
    border-radius: 287px 287px 40px 40px;
    background: linear-gradient(180deg, var(--portrait-light) 0%, #5c534d 45%, var(--portrait-dark) 100%);
    box-shadow: 0 0 30px rgba(0,0,0,0.45);
  }

  .card {
    position: absolute;
    border-radius: 6px;
    box-shadow: 0 4px 10px rgba(0,0,0,0.5);
  }
  .card--back { background: var(--card-cream); }
  .card--face { background: var(--card-white); }
  .card-a { left: 628px; top: 2px; width: 118px; height: 58px; transform: rotate(12deg); }
  .card-c { left: 560px; top: 140px; width: 96px; height: 140px; transform: rotate(-22deg); opacity: 0.8; }
  .card-b { left: 660px; top: 118px; width: 70px; height: 160px; transform: rotate(-28deg); }
  .card-d { left: 6px; top: 912px; width: 118px; height: 150px; transform: rotate(-24deg); }
  .card-e { left: 700px; top: 988px; width: 130px; height: 140px; transform: rotate(32deg); }
  .card-f { left: 850px; top: 912px; width: 36px; height: 100px; transform: rotate(-12deg); }

  .crystal-ball {
    position: absolute;
    left: 271px; top: 474px;
    width: 316px; height: 316px;
    border-radius: 50%;
    background: radial-gradient(circle at 45% 45%, var(--moon-light) 0%, #d6dfe9 45%, var(--moon-shadow) 100%);
    box-shadow: 0 0 40px 14px rgba(210,230,255,0.35);
  }
  .ball-name {
    position: absolute;
    left: 271px; top: 560px;
    width: 316px;
    text-align: center;
    font-family: "Rye", serif;
    font-size: 50px;
    line-height: 66px;
    color: var(--logo-grey);
  }

  .ribbon {
    position: absolute;
    left: 160px; top: 748px;
    width: 566px; height: 118px;
  }
  .ribbon-text {
    position: absolute;
    left: 160px; top: 780px;
    width: 566px;
    text-align: center;
    font-family: "Rye", serif;
    font-size: 34px;
    color: var(--paper-white);
    transform: rotate(-4.5deg);
  }

  .show-date {
    position: absolute;
    left: 0; top: 912px;
    width: 873px;
    text-align: center;
    font-family: "Graduate", serif;
    font-weight: 400;
    font-size: 54px;
    line-height: 70px;
    word-spacing: 10px;
    color: var(--paper-white);
  }
  .show-times {
    position: absolute;
    left: 0; top: 1012px;
    width: 873px;
    text-align: center;
    font-family: "PT Sans", sans-serif;
    font-size: 30px;
    line-height: 40px;
    color: var(--paper-white);
  }

  .esp-symbols {
    position: absolute;
    left: 329px; top: 1104px;
    width: 212px; height: 30px;
  }

  .website {
    position: absolute;
    left: 0; top: 1168px;
    width: 873px;
    text-align: center;
    font-family: "PT Sans", sans-serif;
    font-size: 24px;
    line-height: 30px;
    letter-spacing: 4px;
    color: var(--link-red);
  }
</style>
</head>
<body>
  <main class="poster">
    <div class="scene-backdrop" role="img" aria-label="Dark misty night scene with a gothic mansion and bare trees"></div>

    <div class="card card--back card-a" role="img" aria-label="Flying playing card, patterned back"></div>
    <div class="card card--back card-c" role="img" aria-label="Flying playing cards"></div>
    <div class="card card--back card-b" role="img" aria-label="Flying playing card, patterned back"></div>

    <div class="portrait" role="img" aria-label="Photo of the magician, head and shoulders, hands raised around a glowing crystal ball"></div>

    <div class="crystal-ball" role="img" aria-label="Glowing moon-like crystal ball"></div>
    <div class="ball-name">Mathis<br>Verbeke</div>

    <svg class="ribbon" viewBox="0 0 566 118" aria-hidden="true">
      <path d="M10 30 L470 0 L560 8 L530 50 L566 92 L110 118 L18 112 L48 72 Z" fill="var(--ribbon-red)"/>
      <path d="M10 30 L48 72 L40 34 Z" fill="var(--ribbon-shade)"/>
    </svg>
    <div class="ribbon-text">Magician &amp; Mentalist</div>

    <div class="card card--back card-d" role="img" aria-label="Playing card, ornate back"></div>
    <div class="card card--face card-e" role="img" aria-label="Two of diamonds playing card"></div>
    <div class="card card--face card-f" role="img" aria-label="Playing card at the edge"></div>

    <h1 class="show-date">THURS 22ND DEC</h1>
    <p class="show-times">Doors open: 7pm - Show starts: 8pm</p>

    <svg class="esp-symbols" viewBox="0 0 212 30" aria-label="ESP symbols" role="img">
      <g fill="none" stroke="var(--symbol-grey)" stroke-width="3.5">
        <circle cx="14" cy="15" r="12"/>
        <path d="M62 2 C54 8, 70 12, 62 16 C54 20, 70 24, 62 29"/>
        <rect x="95" y="3" width="24" height="24"/>
        <path d="M149 2 V28 M136 15 H162"/>
        <path d="M198 2 L201.5 11 L211 11 L203.5 17 L206.5 27 L198 21 L189.5 27 L192.5 17 L185 11 L194.5 11 Z"/>
      </g>
    </svg>

    <p class="website">www.mathisverbeke.be</p>
  </main>
</body>
</html>
```